Briefkopf für Verwaltung im Taubertal
Zielgruppe
Die Verwaltungsgemeinschaft Wendelmark setzt sich aus den vier Kommunen zusammen: Stadt Wendelmark, Gemeinde Auenbach, Gemeinde Hollerfeld und Gemeinde Steinwiesen. Als kommunaler Ansprechpartner sprechen wir alle Bürgerinnen und Bürger an.
Aufgabenstellung
Das Logo der Verwaltungsgemeinschaft soll im Briefkopf abgebildet werden. Wesentliche Inhalte wie Adresse, Telefon, Mail, etc. sollen vorhanden sein. Der Briefkopf sollte nach Möglichkeit der DIN-Norm (DIN 5008) entsprechen und Falzmarken enthalten. Der Ausdruck erfolgt vorwiegend in Schwarz-Weiß, nur gelegentlich in Farbe. Daher soll der Briefkopf auch in Schwarz-Weiß Druck optisch ansprechbar wirken und zudem relativ wenig Tonerfarbe verbrauchen. Die Gestaltung soll sowohl neutral, seriös, als auch freundlich wirken.

```html
<!DOCTYPE html>
<html lang="de">
<head>
<meta charset="utf-8">
<title>Briefkopf VGem Wendelmark</title>
<link href="https://fonts.googleapis.com/css2?family=Arimo:wght@400;700&display=swap" rel="stylesheet">
<style>
  :root {
    --backdrop: #e0fdfd;
    --paper: #ffffff;
    --accent: #990000;
    --ink: #111111;
  }
  * { margin: 0; padding: 0; box-sizing: border-box; }
  html, body {
    width: 913px; height: 1200px; overflow: hidden;
    background: var(--backdrop);
    font-family: "Arimo", Arial, sans-serif;
    color: var(--ink);
  }
  .letterhead {
    position: absolute; left: 69px; top: 53px;
    width: 774px; height: 1093px;
    background: var(--paper);
  }
  .accent-bar { position: absolute; height: 5px; width: 303px; background: var(--accent); }
  .accent-bar--top { left: 0; top: 0; }
  .accent-bar--bottom { right: 0; bottom: 0; }
  .brand {
    position: absolute; left: 588px; top: 84px;
    display: flex; align-items: center; gap: 7px;
    font-size: 21px; font-weight: 700; color: var(--accent);
  }
  .brand__dot { width: 14px; height: 14px; border-radius: 50%; background: var(--accent); }
  .contact {
    position: absolute; left: 597px; top: 165px;
    font-size: 11px; line-height: 13.2px;
  }
  .contact p + p { margin-top: 13px; }
  .sender-line {
    position: absolute; left: 76px; top: 222px;
    font-size: 9.5px; text-decoration: underline;
  }
  .footer {
    position: absolute; left: 76px; top: 886px;
    font-size: 11px; line-height: 13.2px;
  }
  .footer p + p { margin-top: 7px; }
</style>
</head>
<body>
  <main class="letterhead">
    <div class="accent-bar accent-bar--top"></div>

    <div class="brand"><span class="brand__dot"></span>Wendelmark</div>

    <div class="contact">
      <p>VGem:09412/5531-0<br>Fax:09412/5531-49<br>E-mail: info@wendelmark.de</p>
      <p>Homepages:<br>www.wendelmark.de<br>www.auenbach.de<br>www.hollerfeld.de<br>www.steinwiesen.de</p>
    </div>

    <div class="sender-line">VGem Wendelmark, Lindenplatz 4, 97300 Wendelmark</div>

    <footer class="footer">
      <p>Korperschaft des offentlichen Rechts<br>Sitz: Lindenplatz 4, 97300 Wendelmark</p>
      <p>Mitgliedsgemeinden:<br>Stadt Wendelmark, Gemeinde Auenbach<br>Gemeinde Hollerfeld, Gemeinde Steinwiesen</p>
      <p>Kreiskasse Talgrund<br>IBAN: DE41 7300 0000 0412 8836 02<br>BIC: KRTGDEW2XTG</p>
      <p>Talbank Hollerfeld<br>IBAN: DE19 7310 0000 0007 2291 45<br>BIC: TLBKDEX3HLF</p>
    </footer>

    <div class="accent-bar accent-bar--bottom"></div>
  </main>
</body>
</html>
```